Webdesign für Stahl- und Brückenbauunternehmen
Zielgruppe
Wir haben 180 Jahre Erfahrung im Stahl- und Brückenbau.
Unsere Auftraggeber ist die öffentliche Hand.
Aufgabenstellung
Das ODLA / TKU-Logo soll mit rein (siehe jetzige Webseite)

```html
<!DOCTYPE html>
<html lang="de">
<head>
<meta charset="utf-8">
<title>VTB Vellbrück Sonderstahlbau</title>
<link rel="stylesheet" href="https://fonts.googleapis.com/css2?family=Merriweather:wght@700&family=Open+Sans:wght@400;600&display=swap">
<style>
:root{
  --blue:#0a7bd0;
  --blue-dark:#0865ad;
  --page:#f0f0f0;
  --white:#ffffff;
  --ink:#333333;
  --muted:#555555;
  --footer:#3d3d3d;
  --line:#999999;
}
*{box-sizing:border-box;margin:0;padding:0}
html,body{width:1200px;height:3488px;overflow:hidden}
body{background:#e6e6e6;font-family:"Open Sans",Arial,sans-serif;color:var(--ink);position:relative}
.page{position:absolute;left:20px;top:20px;width:1155px;height:3468px;background:var(--page);box-shadow:0 0 14px rgba(0,0,0,.12);overflow:hidden}
.abs{position:absolute}
.serif{font-family:"Merriweather",Georgia,serif;font-weight:700}
.brand{font-family:"Open Sans",Arial,sans-serif;font-weight:600;color:var(--blue);display:flex;align-items:center;gap:8px}
.brand .mark{width:18px;height:18px;background:var(--blue)}
.nav{left:335px;top:34px;display:flex;gap:27px;font-size:13px;color:var(--ink)}
.partners{left:946px;top:20px;display:flex;gap:12px;align-items:center}
.partner{display:flex;align-items:center;gap:5px;font-size:11px;font-weight:600;color:var(--blue-dark)}
.partner i{display:block;width:32px;height:24px;background:#1f3f9a}
.partner i.g{background:#7ab648;width:18px}
.hero{left:0;top:75px;width:517px;height:463px;background:var(--blue)}
.hero h1{position:absolute;left:75px;top:186px;color:var(--white);font-size:31px;line-height:40px}
.hero p{position:absolute;left:75px;top:270px;color:var(--white);font-size:13px;line-height:18px;width:330px}
.btn-white{position:absolute;left:75px;top:330px;width:147px;height:49px;background:var(--white);color:var(--blue);font-size:11px;font-weight:600;display:flex;align-items:center;justify-content:center}
.photo{background:linear-gradient(160deg,#c9d6d2,#5d7a5c 45%,#2f4a36 75%,#8a8f6e)}
.badge180{left:546px;top:504px;width:121px;height:118px;background:var(--white);text-align:center;color:var(--blue)}
.badge180 b{display:block;font-weight:400;font-size:48px;line-height:52px;margin-top:12px}
.badge180 span{display:block;font-size:10px;line-height:15px}
.social{left:75px;top:602px;display:flex;gap:22px;font-size:14px;font-weight:600;color:var(--blue)}
.pager{left:262px;top:598px;display:flex;align-items:center;gap:40px;color:var(--ink)}
.pager .n{font-size:26px}.pager .n small{font-size:15px}
.outline{border:1.5px solid var(--blue)}
.label{font-size:12px;color:var(--ink);letter-spacing:.2px}
.h2{color:var(--blue);font-size:31px;line-height:40px}
.body-text{font-size:12.5px;line-height:18px;color:var(--ink)}
.link{font-size:11px;font-weight:600;color:var(--blue)}
.card{background:var(--white);width:256px;box-shadow:0 2px 6px rgba(0,0,0,.06);text-align:center;padding:0 24px}
.card h3{font-weight:400;font-size:17px;line-height:24px;color:var(--ink);margin-top:4px}
.card p{font-size:10px;line-height:16px;color:var(--muted);margin-top:10px}
.card svg{display:block;margin:14px auto 0}
.caption{left:356px;top:2215px;width:453px;height:105px;background:var(--white);box-shadow:0 3px 8px rgba(0,0,0,.15);padding:12px 46px}
.caption h4{font-weight:400;font-size:16px;color:var(--ink)}
.caption p{font-size:11px;line-height:16px;color:var(--muted);margin-top:6px;width:300px}
.caption .link{position:absolute;right:20px;bottom:10px;font-weight:400}
.arrow{font-size:20px;color:var(--ink)}
.btn-blue{background:var(--blue);color:var(--white);font-size:11px;font-weight:600;display:flex;align-items:center;justify-content:center}
.footer{left:0;top:3125px;width:1155px;height:310px;background:var(--footer)}
.bar{left:0;top:3435px;width:1155px;height:33px;background:var(--blue);color:var(--white);font-size:12px}
.bar span{position:absolute;top:11px}
.contact{left:71px;top:3021px;width:526px;height:335px;background:var(--white);border:2px solid var(--blue)}
.contact h2{position:absolute;left:70px;top:28px;color:var(--blue);font-size:31px}
.field{position:absolute;left:70px;width:378px;border-bottom:1px solid var(--line);font-size:11px;color:var(--ink)}
.fmenu{left:698px;top:3240px;color:var(--white);font-size:11.5px;line-height:24.5px}
.finfo{left:874px;top:3263px;color:var(--white);font-size:11.5px;line-height:24.5px}
</style>
</head>
<body>
<div class="page">
  <!-- header -->
  <div class="abs brand" style="left:75px;top:28px;font-size:26px"><span class="mark"></span>VTB</div>
  <nav class="abs nav"><span>Unternehmen</span><span>Leistungen</span><span>Aktuelle Projekte</span><span>Referenzen</span><span>Kontakt</span></nav>
  <div class="abs partners">
    <div class="partner"><i></i>ODLA</div>
    <div class="partner"><i class="g"></i>TKU</div>
  </div>

  <!-- hero -->
  <section class="abs hero">
    <h1 class="serif">Ihr Spezialist für<br>anspruchsvolle Projekte</h1>
    <p>180-jährige traditionsreiche Vergangenheit und Erfahrung im Stahl- und Brückenbau</p>
    <div class="btn-white">MEHR INFO</div>
  </section>
  <div class="abs photo" role="img" aria-label="Stahlbrücke über einem bewaldeten Tal vor Bergen" style="left:517px;top:131px;width:638px;height:519px"></div>
  <div class="abs badge180"><b>180</b><span>JAHRE<br>ERFAHRUNG</span></div>
  <div class="abs social"><span>Fabo</span><span>Lino</span><span>Xando</span></div>
  <div class="abs pager"><span class="arrow">⟵</span><span class="n">2 <small>/ 3</small></span><span class="arrow">⟶</span></div>

  <!-- about -->
  <div class="abs photo" role="img" aria-label="Luftaufnahme des Werksgeländes mit Hallen" style="left:75px;top:732px;width:442px;height:387px;background:linear-gradient(150deg,#9fb5a0,#c9d4d8 40%,#7e8c8e 70%,#5e7a4a)"></div>
  <div class="abs outline" style="left:473px;top:815px;width:80px;height:78px"></div>
  <div class="abs label" style="left:578px;top:817px">ÜBER UNS</div>
  <h2 class="abs serif h2" style="left:578px;top:846px;width:420px">Wenn es keine Brücken auf der Welt gäbe, nützen die ganzen Wege nichts.</h2>
  <p class="abs body-text" style="left:578px;top:995px;width:360px">Die VTB – Vellbrück Sonderstahlbau GmbH wurde am 01.12.2004 durch Ausgliederung aus der VM – Vellbrücker Maschinen- und Anlagenbau GmbH gegründet.</p>
  <div class="abs link" style="left:578px;top:1064px;font-weight:400">MEHR &gt;</div>

  <!-- services -->
  <div class="abs label" style="left:0;width:1155px;text-align:center;top:1215px">UNSERE LEISTUNGEN</div>
  <h2 class="abs serif h2" style="left:0;width:1155px;text-align:center;top:1242px">Wir können Brücke.</h2>
  <div class="abs outline" style="left:960px;top:1505px;width:78px;height:79px"></div>

  <div class="abs card" style="left:169px;top:1370px;height:167px">
    <svg width="50" height="20" viewBox="0 0 50 20" fill="none" stroke="#0a7bd0" stroke-width="2"><path d="M2 16h46M6 16C12 4 38 4 44 16M15 9v7M25 7v9M35 9v7"/></svg>
    <h3>BRÜCKEN</h3>
    <p>In einer modernen Farbgebung wird besonders auf die Untergrundvorbereitung des Stahls wert gelegt.</p>
  </div>
  <div class="abs card" style="left:450px;top:1370px;height:167px">
    <svg width="50" height="20" viewBox="0 0 50 20" fill="none" stroke="#0a7bd0" stroke-width="3"><path d="M2 4h46M14 4v14M36 4v14"/></svg>
    <h3>DOPPELT<br>VORGESPANNTE TRÄGER</h3>
    <p style="margin-top:6px">Die Herstellung von doppelt vorgespannten Trägern sind eine Spezialität der VTB.</p>
  </div>
  <div class="abs card" style="left:730px;top:1370px;height:167px">
    <svg width="50" height="20" viewBox="0 0 50 20" fill="none" stroke="#0a7bd0" stroke-width="3"><path d="M2 4h46M18 4v10h14V4"/></svg>
    <h3>VF-TRÄGER</h3>
    <p style="margin-top:18px">Die Verbundfertigteil-Bauweise stellt eine Alternative zu den Spannbetonträgern dar.</p>
  </div>
  <div class="abs card" style="left:169px;top:1562px;height:178px">
    <svg width="50" height="30" viewBox="0 0 50 30" fill="none" stroke="#0a7bd0" stroke-width="2"><path d="M6 22h30M8 22V12h14l4 10M12 12V6h8v6M36 16l8-4 4 14"/><circle cx="10" cy="26" r="2"/><circle cx="18" cy="26" r="2"/><circle cx="26" cy="26" r="2"/></svg>
    <h3 style="margin-top:10px">BAUMASCHINEN</h3>
    <p>Dieser Fertigungsbereich stellt große Baumaschinenkomponenten mit Stückgewichten bis zu 100 Tonnen her.</p>
  </div>
  <div class="abs card" style="left:450px;top:1562px;height:178px">
    <svg width="50" height="30" viewBox="0 0 50 30" fill="none" stroke="#0a7bd0" stroke-width="2"><path d="M14 8h20l4 4v14H18l-4-4zM14 8l4 4h20M18 12v14M22 18h10"/></svg>
    <h3 style="margin-top:10px">SONDERSTAHLBAU</h3>
    <p>Der Stahlhochbau als Teil des Gebietes ist geprägt von individuellen Konstruktionen.</p>
  </div>
  <div class="abs card" style="left:730px;top:1562px;height:178px">
    <svg width="50" height="30" viewBox="0 0 50 30" fill="none" stroke="#0a7bd0" stroke-width="2"><path d="M14 26L34 6M16 6l20 20M30 4l6 6M12 24l-2 4 4-2"/></svg>
    <h3>MECHANISCHE<br>BEARBEITUNG</h3>
    <p style="margin-top:6px">Von Einzelteilen und Baugruppen sowie die mechanische Endbearbeitung verschiedenster Komponenten ist optimal...</p>
  </div>

  <!-- references -->
  <h2 class="abs serif h2" style="left:0;width:1155px;text-align:center;top:1864px">Referenzen</h2>
  <div class="abs photo" role="img" aria-label="Stahlbrücke über einen Fluss im Nebel" style="left:90px;top:1957px;width:195px;height:302px;background:linear-gradient(180deg,#a9c6d6,#7a99a8 60%,#55656a)"></div>
  <div class="abs photo" role="img" aria-label="Untersicht einer Autobahnbrücke aus Stahl" style="left:306px;top:1959px;width:553px;height:297px;background:linear-gradient(170deg,#b8c2c8,#8a9298 45%,#5f6a5e)"></div>
  <div class="abs photo" role="img" aria-label="Stahlfachwerkbrücke während der Montage mit Kran" style="left:880px;top:1957px;width:195px;height:302px;background:linear-gradient(180deg,#8fb8d0,#5f8aa0 55%,#44565a)"></div>
  <div class="abs caption">
    <h4>ELBTALBRÜCKE NORDHAFEN // 2019</h4>
    <p>Stabbogenbrücke, ca 70,0 x 7,4 x 11,0 m, ca 400 to. Leistungen: Engineering, Fertigung, Beschichtung, Transport, Montage</p>
    <span class="link">DETAILS &gt;</span>
  </div>
  <div class="abs arrow" style="left:258px;top:2278px">⟵</div>
  <div class="abs arrow" style="left:880px;top:2278px">⟶</div>
  <div class="abs btn-blue" style="left:502px;top:2366px;width:147px;height:47px">ALLE ANSEHEN ⟶</div>

  <!-- team -->
  <div class="abs label" style="left:146px;top:2598px">ZUR VERSTÄRKUNG UNSERES TEAM´S SUCHEN WIR</div>
  <h2 class="abs serif h2" style="left:146px;top:2625px">Baue mit uns Deine<br>Brücke in die Zukunft!</h2>
  <p class="abs body-text" style="left:146px;top:2737px;width:380px">Lorem ipsum dolor sit amet, consectetur adipiscing elit. Mauris sed at elit lobortis adipiscing quis id aliquam platea. Blandit eget aenean neque, et orci nisl, non et eu.</p>
  <div class="abs link" style="left:146px;top:2812px;font-weight:400">STELLENANGEBOTE &gt;</div>
  <div class="abs photo" role="img" aria-label="Team bei einer Besprechung am Tisch in einem Loft-Büro" style="left:633px;top:2516px;width:442px;height:387px;background:linear-gradient(160deg,#c8c6c0,#9a8e84 45%,#6f5e55 75%,#b9b4ad)"></div>
  <div class="abs outline" style="left:593px;top:2584px;width:79px;height:79px"></div>

  <!-- footer -->
  <div class="abs footer"></div>
  <div class="abs contact">
    <h2 class="serif">Kontakt</h2>
    <div class="field" style="top:92px;height:38px;padding-top:0">Name</div>
    <div class="field" style="top:136px;height:35px">E-Mail Adresse</div>
    <div class="field" style="top:176px;height:86px">Nachricht</div>
    <div class="btn-blue" style="position:absolute;left:191px;top:287px;width:114px;height:32px">SENDEN ⟶</div>
  </div>
  <div class="abs brand" style="left:874px;top:3175px;font-size:40px;color:var(--blue)"><span class="mark" style="width:26px;height:26px"></span>VTB</div>
  <div class="abs fmenu">
    <div>MENU</div>
    <div style="margin-top:4px">Unternehmen</div><div>Leistungen</div><div>Aktuelle Projekte</div><div>Referenzen</div><div>Kontakt</div>
  </div>
  <div class="abs finfo">
    <div style="font-weight:600">VTB Vellbrück Sonderstahlbau GmbH</div>
    <div>Äußere Lindenstraße 12 // 08123 Vellbrück</div>
    <div>Tel.: 0391 4420 0</div>
    <div>Fax: 0391 4420 202</div>
    <div>E-Mail: info@vtb-stahlbau.example</div>
  </div>
  <div class="abs bar">
    <span style="left:321px">Impressum</span>
    <span style="left:519px">VTB GmbH ©2021</span>
    <span style="left:756px">Datenschutz</span>
  </div>
</div>
</body>
</html>
```